THE POINT AT MAPLE SWALE HUDSON RIVER WATERFRONT LAND

crisp clear business cards on wood stock or thick paper with large font with a river otter logo, PERSONAL INFO ON ONE SIDE, PROJECT INFO ON THE OTHER SIDE
Updates

I don’t have a logo. Just thought that a photo of a river otter would look appealing.

Target Market(s)

Buyers and realtors

Industry/Entity Type

Real Estate Development

Contact Information for Business Card

MARTIN OSGOOD
518-730-4862 (Call or Text)
STONE HAVEN LLC PRINCIPAL

MOSHAVENRD@TARNMAIL.COM

Font styles to use
Sans Serif

Colors
fbfdfe
0792cd
00a990
fbed22
ec1f27

Requirements
Must have
• LARGE FONT, ROUNDED EDGES,
Nice to have
• ON THE BACK SIDE :
• THE POINT AT MAPLE SWALE
• HUDSON RIVER WATERFRONT LAND
• 2 TO 67 ACRES---READY TO BUILD
• PRICED TO SELL!

```html
<!DOCTYPE html>
<html lang="en">
<head>
<meta charset="utf-8">
<title>Martin Osgood – Business Card</title>
<link rel="stylesheet" href="https://fonts.googleapis.com/css2?family=Montserrat:wght@500;700;800;900&family=Oswald:wght@500;600&display=swap">
<style>
  :root {
    --backdrop: #2e2e2e;
    --kraft: #cdae80;
    --kraft-edge: #b8976a;
    --brand-red: #b3141c;
    --brand-green: #1d5b22;
    --paper-white: #fbfdfe;
  }
  * { box-sizing: border-box; margin: 0; padding: 0; }
  html, body { width: 1200px; height: 1200px; overflow: hidden; }
  body {
    background: var(--backdrop);
    font-family: "Montserrat", Arial, sans-serif;
    display: flex;
    flex-direction: column;
    align-items: center;
    justify-content: center;
    gap: 60px;
  }
  .card {
    width: 840px;
    height: 480px;
    border-radius: 28px;
    background: var(--kraft);
    box-shadow: inset 0 0 0 2px var(--kraft-edge), 0 10px 30px rgba(0,0,0,.45);
    position: relative;
    overflow: hidden;
  }

  /* Front: personal info */
  .card--front {
    display: flex;
    flex-direction: column;
    justify-content: center;
    padding: 0 70px;
  }
  .org-mark {
    display: flex;
    align-items: center;
    gap: 16px;
    margin-bottom: 34px;
  }
  .org-mark__dot {
    width: 54px; height: 54px;
    border-radius: 50%;
    background: var(--brand-red);
    flex: none;
  }
  .org-mark__name {
    font-weight: 700;
    font-size: 20px;
    letter-spacing: 2px;
    color: var(--brand-green);
  }
  .person__name {
    font-weight: 900;
    font-size: 66px;
    line-height: 1;
    color: var(--brand-red);
  }
  .person__role {
    font-weight: 700;
    font-size: 24px;
    letter-spacing: 4px;
    color: var(--brand-green);
    margin-top: 12px;
  }
  .contact {
    margin-top: 40px;
    display: flex;
    flex-direction: column;
    gap: 16px;
  }
  .contact__row {
    display: flex;
    align-items: center;
    gap: 14px;
    font-weight: 800;
    font-size: 22px;
    letter-spacing: 1px;
    color: var(--brand-green);
  }
  .contact__note { font-weight: 500; font-size: 16px; letter-spacing: 0; }
  .contact__icon {
    width: 38px; height: 38px;
    border-radius: 50%;
    background: var(--brand-red);
    display: flex; align-items: center; justify-content: center;
    flex: none;
  }

  /* Back: project info */
  .card--back {
    display: flex;
    flex-direction: column;
    justify-content: center;
    padding: 0 70px;
  }
  .project__title {
    font-family: "Oswald", "Arial Narrow", sans-serif;
    font-weight: 600;
    font-size: 84px;
    line-height: 1;
    color: var(--brand-red);
  }
  .project__subtitle {
    font-weight: 900;
    font-size: 37px;
    letter-spacing: 2px;
    color: var(--brand-green);
    margin-top: 10px;
  }
  .project__points {
    list-style: none;
    display: flex;
    gap: 40px;
    margin-top: 30px;
  }
  .project__point {
    display: flex;
    align-items: center;
    gap: 14px;
    font-weight: 800;
    font-size: 22px;
    color: var(--brand-green);
  }
  .project__point::before {
    content: "";
    width: 24px; height: 24px;
    border-radius: 50%;
    background: var(--brand-red);
    flex: none;
  }
</style>
</head>
<body>
  <section class="card card--front" aria-label="Business card front">
    <div class="org-mark">
      <span class="org-mark__dot"></span>
      <span class="org-mark__name">WILLOW BANK NATURE CIRCLE</span>
    </div>
    <h1 class="person__name">MARTIN OSGOOD</h1>
    <p class="person__role">STONE HAVEN LLC PRINCIPAL</p>
    <div class="contact">
      <p class="contact__row">
        <span class="contact__icon">
          <svg width="18" height="20" viewBox="0 0 18 20" aria-hidden="true">
            <rect x="4" y="1" width="10" height="18" rx="2" fill="none" stroke="#fbfdfe" stroke-width="2"/>
            <circle cx="9" cy="15.5" r="1.2" fill="#fbfdfe"/>
          </svg>
        </span>
        518-730-4862 <span class="contact__note">(Call or Text)</span>
      </p>
      <p class="contact__row">
        <span class="contact__icon">
          <svg width="20" height="16" viewBox="0 0 20 16" aria-hidden="true">
            <rect x="1.5" y="2" width="17" height="12" rx="1.5" fill="none" stroke="#fbfdfe" stroke-width="2"/>
            <path d="M2 3 L10 9.5 L18 3" fill="none" stroke="#fbfdfe" stroke-width="2"/>
          </svg>
        </span>
        MOSHAVENRD@TARNMAIL.COM
      </p>
    </div>
  </section>

  <section class="card card--back" aria-label="Business card back">
    <h2 class="project__title">THE POINT AT MAPLE SWALE</h2>
    <p class="project__subtitle">HUDSON RIVER WATERFRONT LAND</p>
    <ul class="project__points">
      <li class="project__point">2 TO 67 ACRES - READY TO BUILD</li>
      <li class="project__point">PRICED TO SELL!</li>
    </ul>
  </section>
</body>
</html>
```